Website design for an Online pastry shop

Website Name : www.lanternandplum.com

Description of the website and its target audience
We are a premium pastry company producing delicious cakes, macarons, cookies, gelato, and other sweet dessert. Our differentiation is that our products are freshly produced with premium quality imported ingredients and one bite into our products set us apart from other bakery shop. We online retail online so as to provide high quality products at a affordable cost. Our products has received raving reviews by many food enthusiast even the hard to please ones. The products contain more natural ingredients and we do not add preservatives. The return rates for our pastry is almost 80%. You only need to try once to be return customers. Our greatest challenge is getting customer to take the first bite. We are so sure of our products that we are going to give people free food tasting.

We are based in China but all our products are developed by award winning chefs from 5 stars hotel. The target customer is woman 16 to 40+ in china. Working class ladies and demand high quality products. A modern, sophisticated and minimalist website

This is a competitive market and image is crucial for such a food ‘conscious ’ orientated customer. They want to feel that they are buying from a reliable company that take great effort to ensure food cleaniness and safety yet affordable price. We make almost 98% of sub ingredients ourselves and we make it by hand.

Style/theme ideas for the web page design
I am looking for a elegant a little rustic, handmade feel yet sophisticated design - one that is easy to the eye yet functional and easy for the user to navigate through. Good play of fonts to give let it feel unique and customised. Black and white is our corporate colours. However, we do not want black background as it does not tease the taste bud. All our colours should come from our products. Customers should be very close to our products. They eat with their eyes first. Black and white is just accent.

Inspirational and competitors websites
http://www.47torte.com/ ( Key competitor )
I like the simple, clean look. The products are the key focus
https://www.pleemo.com/
clean, fresh and different. Attractive with purpose. Feminine
http://quillandbobbin.com/
this has a great layout - lots of information and nicely presented. Very sweet and feminine
http://www.storehavenrow.com/
product features is the focus
http://www.odettevulmers.com/store/
fun, feminine, rustic

Number of pages needed : 6 ( Uncoded PSD design only )
Page descriptions
Home Page - This page will show what makes our products stand out from the competitors and provide an introduction of who we are.
2nd page : Product catalogue
3nd page: Detail Product page with pictures and descriptions. Select products size and add to cart....
4rd page: Brand Story with pictures and descriptions.
5th page Contact Us : Here they can contact or schedule an appointment for free product tasting
6th page : Check out page

Target Market(s)

Female, Asian, Working Class, Office

Industry/Entity Type

Shop

Number of Pages Required

5+ page

Font styles to use
Other font styles liked:
• See packaging

Requirements
Must have
• Please see the project wire frame file " main page.png " or file number 70

```html
<!DOCTYPE html>
<html lang="en">
<head>
<meta charset="utf-8">
<title>Lantern &amp; Plum — Artisan Pastry</title>
<link rel="stylesheet" href="https://fonts.googleapis.com/css2?family=Roboto:wght@300;400&display=swap">
<style>
  :root {
    --ink: #1d1d1d;
    --white: #ffffff;
    --accent: #f07a52;
    --hero-bg: #f1eef6;
    --berry: rgba(128, 22, 42, 0.62);
    --cream: rgba(240, 214, 150, 0.55);
    --dark: #2b2b2b;
    --darker: #3a3a3a;
    --field: #3b3b3b;
    --facet: #2a7fc1;
    --warble: #3aa1e0;
    --gather: #f3724a;
    --muted: #9a9a9a;
  }
  * { box-sizing: border-box; margin: 0; padding: 0; }
  html, body { width: 1012px; height: 1200px; overflow: hidden; background: var(--white); }
  body { font-family: "Roboto", "Helvetica Neue", Arial, sans-serif; font-weight: 300; color: var(--ink); position: relative; }
  a { text-decoration: none; }

  /* Hero */
  .hero { position: absolute; left: 0; top: 0; width: 1012px; height: 546px; background: var(--hero-bg); overflow: hidden; }
  .hero-photo { position: absolute; inset: 0;
    background:
      radial-gradient(ellipse 360px 200px at 50% 32%, var(--berry) 0%, rgba(128,22,42,0.25) 55%, transparent 100%),
      radial-gradient(ellipse 420px 240px at 55% 66%, var(--cream) 0%, rgba(240,214,150,0.2) 60%, transparent 100%),
      linear-gradient(135deg, #f8f6fb, var(--hero-bg)); }
  .site-header { position: absolute; left: 0; top: 0; width: 100%; height: 110px; }
  .header-tools { position: absolute; left: 22px; top: 18px; display: flex; gap: 14px; }
  .cart-count { position: absolute; left: 48px; top: -3px; width: 10px; height: 10px; border-radius: 50%; background: var(--accent); }
  .brand { position: absolute; left: 0; width: 100%; top: 84px; text-align: center; color: var(--white); font-size: 20px; font-weight: 400; letter-spacing: 0.5px; }
  .brand-dot { display: block; width: 30px; height: 30px; margin: -60px auto 16px; border-radius: 50%; background: var(--white); }
  .menu-toggle { position: absolute; right: 24px; top: 22px; }
  .hero-copy { position: absolute; left: 26px; top: 424px; font-size: 20px; line-height: 30px; font-weight: 300; color: #2a2a2a; }
  .read-more { display: inline-flex; align-items: center; gap: 8px; font-size: 10px; color: var(--accent); font-weight: 400; }
  .hero .read-more { position: absolute; left: 256px; top: 511px; }

  /* About */
  .about { position: absolute; left: 0; top: 546px; width: 1012px; height: 244px; background: var(--white); }
  .about-photo { position: absolute; left: 0; top: 0; width: 640px; height: 244px;
    background: linear-gradient(to right, #e7c9b0 0%, #e9b48f 35%, #efe4df 70%, var(--white) 100%); }
  .about-copy { position: absolute; right: 16px; top: 64px; text-align: right; font-size: 20px; line-height: 30px; }
  .about .read-more { position: absolute; right: 20px; top: 191px; }

  /* Categories */
  .categories { position: absolute; left: 0; top: 790px; width: 1012px; height: 253px; display: flex; }
  .category { position: relative; width: 253px; height: 253px; }
  .category-cakes { background: linear-gradient(160deg, #efe9e3, #d8d3dc 55%, #c9c4cf); }
  .category-macarons { background: linear-gradient(135deg, #4a2f22, #3a251b 60%, #2d1c15); }
  .category-cookies { background: linear-gradient(160deg, #e9ddd0, #dcc9b4 60%, #cfb9a1); }
  .category-gelato { background: linear-gradient(160deg, #eeeae6, #e4dcd6 60%, #e7d3d4); }
  .category-frame { position: absolute; left: 25px; top: 26px; width: 208px; height: 208px; border: 2px solid var(--ink); display: flex; align-items: center; justify-content: center; font-size: 27px; color: var(--ink); }

  /* Newsletter & social */
  .connect { position: absolute; left: 0; top: 1043px; width: 1012px; height: 109px; display: flex; }
  .mailing { width: 571px; background: var(--dark); display: flex; align-items: center; padding-left: 26px; }
  .mailing-title { color: var(--white); font-size: 20px; width: 206px; }
  .mailing-input { width: 325px; height: 34px; background: var(--field); color: var(--muted); font-size: 10px; padding-left: 10px; display: flex; align-items: center; }
  .follow { width: 110px; background: var(--white); display: flex; align-items: center; justify-content: center; text-align: center; font-size: 14px; line-height: 22px; }
  .social { width: 110px; display: flex; align-items: center; justify-content: center; color: var(--white); font-size: 15px; font-weight: 400; }
  .social-facet { background: var(--facet); }
  .social-warble { background: var(--warble); }
  .social-gather { background: var(--gather); width: 111px; }

  .site-footer { position: absolute; left: 0; top: 1152px; width: 1012px; height: 48px; background: var(--darker); color: #e0e0e0; font-size: 11px; display: flex; align-items: center; justify-content: center; }
</style>
</head>
<body>
  <section class="hero">
    <div class="hero-photo" role="img" aria-label="Cheesecake topped with glossy strawberry compote on a biscuit base"></div>
    <header class="site-header">
      <div class="header-tools">
        <svg width="18" height="20" viewBox="0 0 18 20" aria-label="Account"><circle cx="9" cy="6" r="4.5" fill="none" stroke="#1d1d1d" stroke-width="1.3"/><path d="M1.5 19c0-4.5 3.3-7 7.5-7s7.5 2.5 7.5 7z" fill="none" stroke="#1d1d1d" stroke-width="1.3"/></svg>
        <svg width="22" height="20" viewBox="0 0 22 20" aria-label="Cart"><path d="M1 2h3l3 11h11l2-8H6" fill="none" stroke="#1d1d1d" stroke-width="1.3"/><circle cx="8.5" cy="17" r="1.5" fill="#1d1d1d"/><circle cx="16.5" cy="17" r="1.5" fill="#1d1d1d"/></svg>
        <span class="cart-count"></span>
      </div>
      <div class="brand"><span class="brand-dot"></span>Lantern &amp; Plum</div>
      <svg class="menu-toggle" width="20" height="14" viewBox="0 0 20 14" aria-label="Menu"><path d="M0 1h20M0 7h20M0 13h20" stroke="#1d1d1d" stroke-width="1.5"/></svg>
    </header>
    <h1 class="hero-copy">The awesomest cheesecake with<br>strawberries you’ve ever seen</h1>
    <a class="read-more">Read more
      <svg width="17" height="17" viewBox="0 0 17 17"><circle cx="8.5" cy="8.5" r="7.8" fill="none" stroke="#f07a52"/><path d="M7 5l3.5 3.5L7 12" fill="none" stroke="#f07a52"/></svg>
    </a>
  </section>

  <section class="about">
    <div class="about-photo" role="img" aria-label="Hand lifting a meringue over a tray of assorted colourful pastries"></div>
    <p class="about-copy">We value flavor over fuss.<br>Artisan, handcrafted and&nbsp; other gourmet<br>confections delivered direct to your door</p>
    <a class="read-more">Read more about us
      <svg width="17" height="17" viewBox="0 0 17 17"><circle cx="8.5" cy="8.5" r="7.8" fill="none" stroke="#f07a52"/><path d="M7 5l3.5 3.5L7 12" fill="none" stroke="#f07a52"/></svg>
    </a>
  </section>

  <nav class="categories">
    <div class="category category-cakes" role="img" aria-label="Blueberry cheesecake on a white plate"><span class="category-frame">Cakes</span></div>
    <div class="category category-macarons" role="img" aria-label="Colourful macarons arranged on dark wood"></div>
    <div class="category category-cookies" role="img" aria-label="Butter cookies on a wooden table"><span class="category-frame">Cookies</span></div>
    <div class="category category-gelato" role="img" aria-label="Gelato macaron sandwich on a plate"><span class="category-frame">Gelato</span></div>
  </nav>

  <section class="connect">
    <div class="mailing">
      <span class="mailing-title">Join our mailing list</span>
      <span class="mailing-input">your e-mail</span>
    </div>
    <div class="follow">FOLLOW<br>US</div>
    <a class="social social-facet">Facet</a>
    <a class="social social-warble">Warble</a>
    <a class="social social-gather">Gather</a>
  </section>

  <footer class="site-footer">©2015</footer>
</body>
</html>
```